Home change of address

Martin & Priya Colwell
WE HAVE MOVED
The address of our new home is
Birch Hollow
47 Thornbury Lane Road
Ashcombe on Wend
Warwickshire
B72 8QT
Tel: 07912 384071
Email: martin@pelmora.uk.com

```html
<!DOCTYPE html>
<html lang="en">
<head>
<meta charset="utf-8">
<title>Martin &amp; Priya Colwell – We Have Moved</title>
<link rel="stylesheet" href="https://fonts.googleapis.com/css2?family=Great+Vibes&family=Signika:wght@400;600;700&display=swap">
<style>
  :root {
    --board: #2d2b2c;
    --paper: #f6faf0;
    --wash: #dcebc6;
    --wash-soft: #e9f2dc;
    --olive: #667a2c;
    --ink: #232323;
    --leaf-core: rgba(92, 124, 52, 0.78);
    --leaf-mid: rgba(128, 158, 80, 0.5);
    --leaf-edge: rgba(150, 178, 104, 0);
    --door: #f7d846;
    --door-deep: #eebf2c;
    --stone: #c2ad96;
  }
  * { margin: 0; padding: 0; box-sizing: border-box; }
  html, body { width: 1200px; height: 1200px; overflow: hidden; background: var(--board); }
  .board { position: relative; width: 1200px; height: 1200px; background: var(--board); }

  .piece {
    position: absolute;
    overflow: hidden;
    background:
      radial-gradient(ellipse 55% 45% at 85% 20%, var(--wash) 0%, transparent 70%),
      radial-gradient(ellipse 60% 40% at 60% 85%, var(--wash) 0%, transparent 70%),
      radial-gradient(ellipse 40% 50% at 95% 60%, var(--wash-soft) 0%, transparent 70%),
      var(--paper);
    box-shadow: 0 6px 14px rgba(0,0,0,0.35);
    font-family: "Signika", "Fira Sans", sans-serif;
    color: var(--ink);
  }
  .flyer { left: 68px; top: 200px; width: 585px; height: 820px; }
  .card-small { left: 788px; top: 376px; width: 258px; height: 154px; }
  .card-large { left: 702px; top: 584px; width: 429px; height: 291px; }

  .foliage, .door { position: absolute; }
  .foliage {
    z-index: 2;
    background: radial-gradient(ellipse closest-side at 50% 50%,
      var(--leaf-core) 0%, var(--leaf-mid) 55%, var(--leaf-edge) 100%);
  }
  .door {
    z-index: 1;
    background:
      linear-gradient(180deg, transparent 0%, transparent 93%, var(--stone) 93%, var(--stone) 100%),
      linear-gradient(180deg, var(--door) 0%, var(--door-deep) 100%);
    border-radius: 2px;
  }

  .line {
    position: absolute;
    z-index: 3;
    right: var(--pad);
    text-align: right;
    white-space: nowrap;
  }
  .names { font-family: "Great Vibes", cursive; color: var(--ink); }
  .headline { font-weight: 700; color: var(--olive); letter-spacing: 0.01em; }
  .home-name { font-weight: 700; }

  .flyer { --pad: 22px; }
  .flyer .names { font-size: 37px; line-height: 44px; }
  .flyer .headline { font-size: 68px; line-height: 64px; }
  .flyer .lead { font-size: 24px; line-height: 28px; }
  .flyer .home-name { font-size: 31px; line-height: 36px; }
  .flyer .address { font-size: 23px; line-height: 28px; }
  .flyer .contact { font-size: 24px; line-height: 28px; }

  .card-large { --pad: 19px; }
  .card-large .names { font-size: 16px; line-height: 20px; }
  .card-large .headline { font-size: 33px; line-height: 36px; }
  .card-large .lead, .card-large .address, .card-large .contact { font-size: 12px; line-height: 14px; }
  .card-large .home-name { font-size: 15px; line-height: 18px; }

  .card-small { --pad: 19px; }
  .card-small .names { font-size: 10px; line-height: 12px; }
  .card-small .headline { font-size: 19px; line-height: 22px; }
  .card-small .lead { font-size: 7px; line-height: 8px; }
  .card-small .home-name { font-size: 9px; line-height: 10px; }
  .card-small .address, .card-small .contact { font-size: 6.5px; line-height: 8px; }
</style>
</head>
<body>
<main class="board">

  <section class="piece flyer">
    <div class="door" role="img" aria-label="Watercolour yellow front door on a stone step" style="left:56px;top:320px;width:160px;height:362px;"></div>
    <div class="foliage" role="img" aria-label="Watercolour olive branches with dark olives" style="left:-130px;top:-120px;width:580px;height:340px;"></div>
    <div class="foliage" role="img" aria-label="Watercolour olive branch with dark olives" style="left:-120px;top:195px;width:340px;height:270px;"></div>

    <div class="line names" style="top:101px;">Martin &amp; Priya Colwell</div>
    <div class="line headline" style="top:166px;">WE HAVE</div>
    <div class="line headline" style="top:229px;">MOVED</div>
    <div class="line lead" style="top:369px;">The address of our new home is</div>
    <div class="line home-name" style="top:411px;">Birch Hollow</div>
    <div class="line address" style="top:460px;">47 Thornbury Lane Road</div>
    <div class="line address" style="top:494px;">Ashcombe on Wend</div>
    <div class="line address" style="top:528px;">Warwickshire</div>
    <div class="line address" style="top:562px;">B72 8QT</div>
    <div class="line contact" style="top:609px;">Tel: 07912 384071</div>
    <div class="line contact" style="top:650px;">Email: martin@pelmora.uk.com</div>
  </section>

  <section class="piece card-small">
    <div class="door" role="img" aria-label="Watercolour yellow front door" style="left:52px;top:59px;width:36px;height:84px;"></div>
    <div class="foliage" role="img" aria-label="Watercolour olive branches" style="left:-40px;top:-36px;width:170px;height:100px;"></div>
    <div class="foliage" role="img" aria-label="Watercolour olive branch" style="left:-36px;top:52px;width:100px;height:86px;"></div>

    <div class="line names" style="top:19px;">Martin &amp; Priya Colwell</div>
    <div class="line headline" style="top:33px;">WE HAVE MOVED</div>
    <div class="line lead" style="top:57px;">The address of our new home is</div>
    <div class="line home-name" style="top:68px;">Birch Hollow</div>
    <div class="line address" style="top:79px;">47 Thornbury Lane Road</div>
    <div class="line address" style="top:88px;">Ashcombe on Wend</div>
    <div class="line address" style="top:96px;">Warwickshire</div>
    <div class="line address" style="top:105px;">B72 8QT</div>
    <div class="line contact" style="top:116px;">Tel: 07912 384071</div>
    <div class="line contact" style="top:126px;">Email: martin@pelmora.uk.com</div>
  </section>

  <section class="piece card-large">
    <div class="door" role="img" aria-label="Watercolour yellow front door on a stone step" style="left:100px;top:117px;width:68px;height:159px;"></div>
    <div class="foliage" role="img" aria-label="Watercolour olive branches with dark olives" style="left:-70px;top:-60px;width:330px;height:190px;"></div>
    <div class="foliage" role="img" aria-label="Watercolour olive branch with dark olives" style="left:-60px;top:110px;width:180px;height:150px;"></div>

    <div class="line names" style="top:41px;">Martin &amp; Priya Colwell</div>
    <div class="line headline" style="top:66px;">WE HAVE MOVED</div>
    <div class="line lead" style="top:112px;">The address of our new home is</div>
    <div class="line home-name" style="top:129px;">Birch Hollow</div>
    <div class="line address" style="top:151px;">47 Thornbury Lane Road</div>
    <div class="line address" style="top:167px;">Ashcombe on Wend</div>
    <div class="line address" style="top:183px;">Warwickshire</div>
    <div class="line address" style="top:199px;">B72 8QT</div>
    <div class="line contact" style="top:220px;">Tel: 07912 384071</div>
    <div class="line contact" style="top:240px;">Email: martin@pelmora.uk.com</div>
  </section>

</main>
</body>
</html>
```